Wine label design for my wife. Wine called "The Marisse"

I need a wine label face lift of one of my premium wines in my collection. My wine sells in Harbor Pell's all over the States. My current label is called The Marisse (my wife's name) and the illustration of her eyes is done by a well know artist from South Africa. I do not have to use this illustration and therefor I attached several pictures of her and her eyes, even when she was a little girl. The wine's also made in South Africa. This is a premium wine that we only sell 2000 bottles per year. The wine sells at 60 usd per bottle, The current label is too white. I also think her eyes should look more at the person buying it, than away from them.

Target Market(s)

Top end wine buyers

Font styles to use
Decorative
Script

Requirements
Must have
• 'The Marisse' must be on the label
An illustration must be on the label
Basically all the info that's on the current label must be on by law. As per Sample
Nice to have
• Maybe some ideas of her whole face?
Should not have
• any gold colour

```html
<!DOCTYPE html>
<html lang="en">
<head>
<meta charset="utf-8">
<title>The Marisse Sauvignon Blanc — Label</title>
<link rel="stylesheet" href="https://fonts.googleapis.com/css2?family=Parisienne&family=Playfair+Display:wght@400&display=swap">
<style>
  :root {
    --backdrop: #333333;
    --label: #2a2a2a;
    --label-edge: #262626;
    --accent: #c4c6ca;
    --accent-dark: #7d8086;
    --band: #8a1f2b;
    --band-dark: #5c131c;
    --type-light: #e4e4e4;
    --band-light: #f4f4f4;
    --band-shade: #c9c9c9;
  }
  * { margin: 0; padding: 0; box-sizing: border-box; }
  html, body {
    width: 1200px;
    height: 901px;
    overflow: hidden;
    background: var(--backdrop);
  }
  .canvas {
    position: relative;
    width: 1200px;
    height: 901px;
    background: var(--backdrop);
  }
  .label {
    position: absolute;
    left: 330px;
    top: 40px;
    width: 540px;
    height: 820px;
    background: var(--label);
    border: 1px solid var(--label-edge);
    text-align: center;
  }
  .label__name {
    position: absolute;
    left: 0;
    right: 0;
    top: 190px;
    font-family: "Parisienne", cursive;
    font-weight: 400;
    font-size: 92px;
    line-height: 1;
    white-space: nowrap;
    color: var(--accent);
  }
  .label__band {
    position: absolute;
    left: 0;
    right: 0;
    height: 30px;
    background: linear-gradient(180deg, var(--band) 0%, var(--band-dark) 50%, var(--band) 100%);
  }
  .label__band--top { top: 350px; }
  .label__band--bottom { top: 470px; }
  .label__portrait {
    position: absolute;
    left: 0;
    right: 0;
    top: 380px;
    height: 90px;
    background: linear-gradient(90deg, var(--band-shade) 0%, var(--band-light) 30%, var(--band-light) 70%, var(--band-shade) 100%);
  }
  .label__variety {
    position: absolute;
    left: 0;
    right: 0;
    top: 548px;
    font-family: "Playfair Display", serif;
    font-size: 42px;
    letter-spacing: 0.5px;
    color: var(--type-light);
  }
  .label__producer {
    position: absolute;
    left: 0;
    right: 0;
    top: 612px;
    font-family: "Playfair Display", serif;
    font-size: 16px;
    letter-spacing: 1px;
    color: var(--accent);
  }
</style>
</head>
<body>
  <main class="canvas">
    <section class="label">
      <h1 class="label__name">The Marisse</h1>
      <div class="label__band label__band--top"></div>
      <div class="label__portrait" role="img" aria-label="Black ink illustration of a woman's eyes looking out at the viewer"></div>
      <div class="label__band label__band--bottom"></div>
      <p class="label__variety">SAUVIGNON BLANC</p>
      <p class="label__producer">DANIEL REYNE WINES</p>
    </section>
  </main>
</body>
</html>
```